Banner Design

We need a banner to display at various locations around the community to promote our gymnastics club. Please see our plumivox page for more photos.

It should be horizontal 76cm X 183cm

```html
<!DOCTYPE html>
<html lang="en">
<head>
<meta charset="utf-8">
<title>Join in the Fun – Gymsports Banner</title>
<link rel="stylesheet" href="https://fonts.googleapis.com/css2?family=Anton&family=Archivo+Black&family=Roboto+Condensed:wght@400;700&display=swap">
<style>
  :root {
    --navy: #2b3a6e;
    --navy-dark: #1f2b55;
    --green: #6cc04a;
    --green-dark: #3f8a2c;
    --white: #ffffff;
    --page: #f2f2f2;
    --photo-a: #5a2a5e;
    --photo-b: #b23a4a;
    --photo-c: #2b2f4f;
  }
  * { margin: 0; padding: 0; box-sizing: border-box; }
  html, body { width: 800px; height: 1200px; overflow: hidden; background: var(--page); }
  .banner {
    position: absolute; left: 20px; top: 332px;
    width: 760px; height: 536px;
    background: var(--white);
    box-shadow: 14px 16px 22px rgba(0,0,0,.45);
    overflow: hidden;
    font-family: "Roboto Condensed", sans-serif;
  }
  .banner-shapes { position: absolute; inset: 0; }
  .headline-join, .headline-fun {
    position: absolute;
    font-family: "Anton", sans-serif;
    line-height: 1;
    background: linear-gradient(180deg, var(--green) 0%, var(--green) 45%, var(--navy) 100%);
    -webkit-background-clip: text; background-clip: text;
    color: transparent;
    -webkit-text-stroke: 3px var(--navy);
  }
  .headline-join { left: 34px; top: 14px; font-size: 108px; letter-spacing: -3px; background: linear-gradient(180deg, var(--green) 0%, var(--green-dark) 100%); -webkit-background-clip: text; background-clip: text; }
  .headline-fun { left: 92px; top: 108px; font-size: 172px; letter-spacing: -2px; }
  .headline-tag {
    position: absolute; left: 237px; top: 24px; width: 124px; height: 97px;
    background: var(--navy); color: var(--white);
    font-family: "Archivo Black", sans-serif; font-size: 40px; line-height: 46px;
    padding: 2px 0 0 10px;
  }
  .headline-tag span { display: block; }
  .headline-tag .tag-the { text-align: right; padding-right: 4px; }
  .class-list { position: absolute; top: 304px; list-style: none; color: var(--navy); font-size: 20px; }
  .class-list li { height: 29px; display: flex; align-items: center; gap: 10px; }
  .class-list svg { width: 17px; height: 17px; flex: none; }
  .class-list.col-left { left: 18px; }
  .class-list.col-right { left: 196px; }
  .info-text { position: absolute; left: 37px; top: 431px; color: var(--white); font-size: 16px; line-height: 21px; }
  .info-text strong { font-weight: 700; font-size: 17px; }
  .contact-row { position: absolute; left: 34px; top: 484px; display: flex; align-items: center; color: var(--white); font-size: 13px; }
  .contact-item { display: flex; align-items: center; gap: 8px; margin-right: 26px; }
  .contact-item svg { width: 24px; height: 24px; }
  .brand-name {
    position: absolute; left: 535px; top: 448px; width: 200px; text-align: center;
    font-family: "Roboto Condensed", sans-serif; font-weight: 700; font-size: 27px;
    color: var(--navy);
  }
</style>
</head>
<body>
<div class="banner">
  <svg class="banner-shapes" viewBox="0 0 760 536" width="760" height="536">
    <defs>
      <linearGradient id="photoTone" x1="0" y1="0" x2="1" y2="1">
        <stop offset="0" stop-color="var(--photo-a)"/>
        <stop offset=".5" stop-color="var(--photo-b)"/>
        <stop offset="1" stop-color="var(--photo-c)"/>
      </linearGradient>
    </defs>
    <path d="M410 0 C360 150 420 360 560 392 C640 410 710 402 760 392 L760 0 Z" fill="url(#photoTone)" role="img" aria-label="Photo of a cheerleading team performing a stunt pyramid on a competition stage"/>
    <path d="M400 0 C350 150 410 360 550 394" fill="none" stroke="var(--green)" stroke-width="9"/>
    <path d="M470 360 C520 396 560 402 620 405 C680 408 720 402 760 396" fill="none" stroke="var(--navy)" stroke-width="12"/>
    <path d="M0 420 L470 420 C515 424 540 480 532 536 L0 536 Z" fill="var(--navy)"/>
  </svg>

  <div class="headline-join">JOIN</div>
  <div class="headline-tag"><span>IN</span><span class="tag-the">THE</span></div>
  <div class="headline-fun">FUN</div>

  <ul class="class-list col-left">
    <li><svg viewBox="0 0 20 20"><polygon points="10,1 12.6,7 19,7.4 14,11.6 15.6,18.5 10,14.8 4.4,18.5 6,11.6 1,7.4 7.4,7" fill="var(--green)"/></svg>Recreational Gym</li>
    <li><svg viewBox="0 0 20 20"><polygon points="10,1 12.6,7 19,7.4 14,11.6 15.6,18.5 10,14.8 4.4,18.5 6,11.6 1,7.4 7.4,7" fill="var(--green)"/></svg>Comprtitive Gym</li>
    <li><svg viewBox="0 0 20 20"><polygon points="10,1 12.6,7 19,7.4 14,11.6 15.6,18.5 10,14.8 4.4,18.5 6,11.6 1,7.4 7.4,7" fill="var(--green)"/></svg>Boys Program</li>
    <li><svg viewBox="0 0 20 20"><polygon points="10,1 12.6,7 19,7.4 14,11.6 15.6,18.5 10,14.8 4.4,18.5 6,11.6 1,7.4 7.4,7" fill="var(--green)"/></svg>Kinder Gym</li>
  </ul>
  <ul class="class-list col-right">
    <li><svg viewBox="0 0 20 20"><polygon points="10,1 12.6,7 19,7.4 14,11.6 15.6,18.5 10,14.8 4.4,18.5 6,11.6 1,7.4 7.4,7" fill="var(--green)"/></svg>Tumbling</li>
    <li><svg viewBox="0 0 20 20"><polygon points="10,1 12.6,7 19,7.4 14,11.6 15.6,18.5 10,14.8 4.4,18.5 6,11.6 1,7.4 7.4,7" fill="var(--green)"/></svg>Cheerleading</li>
    <li><svg viewBox="0 0 20 20"><polygon points="10,1 12.6,7 19,7.4 14,11.6 15.6,18.5 10,14.8 4.4,18.5 6,11.6 1,7.4 7.4,7" fill="var(--green)"/></svg>Tricking</li>
    <li><svg viewBox="0 0 20 20"><polygon points="10,1 12.6,7 19,7.4 14,11.6 15.6,18.5 10,14.8 4.4,18.5 6,11.6 1,7.4 7.4,7" fill="var(--green)"/></svg>Parkour</li>
  </ul>

  <p class="info-text">For enrolment details and further information on these and<br>more classes visit: <strong>www.vaultagymsports.com</strong></p>

  <div class="contact-row">
    <span class="contact-item">
      <svg viewBox="0 0 24 24"><polygon points="12,1 15,8.5 23,9 17,14 19,22.5 12,18 5,22.5 7,14 1,9 9,8.5" fill="var(--white)"/><path d="M10 10.5 c-.6 1.8.8 4 2.6 4.6 l.8-1 1.4.8-.6 1.3 c-2.6-.2-5-2.8-5.2-5.3 l1.2-.6.8 1.3z" fill="var(--green)"/></svg>
      (02) 9000 1234
    </span>
    <span class="contact-item">
      <svg viewBox="0 0 24 24"><polygon points="12,1 15,8.5 23,9 17,14 19,22.5 12,18 5,22.5 7,14 1,9 9,8.5" fill="var(--white)"/><path d="M12 8.5 a2.6 2.6 0 0 1 2.6 2.6 c0 2-2.6 4.6-2.6 4.6 s-2.6-2.6-2.6-4.6 A2.6 2.6 0 0 1 12 8.5z" fill="var(--green)"/></svg>
      12-14 Fenwick Place Elmsdale
    </span>
  </div>

  <div class="brand-name">Vaulta Gymsports</div>
</div>
</body>
</html>
```